Luxury Business Card Design for High-End Window Treatments

Gilded Vantages
Custom Plantation Shutters & Architectural Shading Systems

⸻

BACK

Daniel Forsythe
Owner

Custom Interior & Exterior Window Treatments

919-482-7034
gildedvantages.com

I have included a picture that I’m hoping we can use on the back, but I’m also wondering if you can get rid of the ladder? Should we get rid of shutters , shades and blinds underneath Gilded Vantages?

Target Market(s)

High-end residential homeowners, custom home builders, architects, interior designers, and luxury renovation clients seeking premium plantation shutters and motorized architectural shading systems.

Industry/Entity Type

Custom Window treatments

Contact Information for Business Card

Front Gilded Vantages Custom Plantation Shutters Motorized Architectural Shading Systems BACK Daniel Forsythe Owner 919-482-7034 GildedVantages.com Custom Interior & Exterior Window Treatments By Appointment

Requirements
Nice to have
• Not 100% sure on nice to halves or the color but you can definitely check out my website to get a better understanding of what I’m trying to do

```html
<!DOCTYPE html>
<html lang="en">
<head>
<meta charset="UTF-8">
<title>Gilded Vantages — Business Card</title>
<link href="https://fonts.googleapis.com/css2?family=Poppins:wght@300;400;600&display=swap" rel="stylesheet">
<style>
  :root {
    --stage: #2b2b2b;
    --card: #141414;
    --emboss: #2c2c2c;
    --gold: #c9a646;
    --gold-light: #e2c86d;
    --white: #f2f2f2;
    --sky: #6f9fd6;
    --slate: #3b4250;
    --foliage: #6f7f3f;
  }
  * { margin: 0; padding: 0; box-sizing: border-box; }
  html, body { width: 1200px; height: 875px; overflow: hidden; }
  body {
    background: var(--stage);
    font-family: "Poppins", sans-serif;
    display: flex;
    align-items: center;
    justify-content: center;
    gap: 60px;
  }
  .card {
    position: relative;
    width: 520px;
    height: 297px;
    background: var(--card);
    border-radius: 18px;
    overflow: hidden;
  }
  /* Front */
  .card-front { border-bottom: 5px solid var(--gold); }
  .front-wordmark {
    position: absolute;
    inset: 0;
    display: flex;
    align-items: center;
    justify-content: center;
    font-size: 46px;
    font-weight: 400;
    color: var(--emboss);
    letter-spacing: 0.5px;
  }
  /* Back */
  .back-art { position: absolute; inset: 0; width: 520px; height: 297px; }
  .back-wordmark {
    position: absolute;
    left: 36px;
    top: 120px;
    font-size: 30px;
    font-weight: 400;
    color: var(--gold);
    line-height: 1.1;
  }
  .contact { position: absolute; left: 36px; bottom: 28px; }
  .contact-name { font-size: 19px; font-weight: 600; color: var(--gold); }
  .contact-role { font-size: 11px; font-weight: 300; color: var(--white); margin-bottom: 8px; }
  .contact-line {
    display: flex;
    align-items: center;
    gap: 8px;
    font-size: 11.5px;
    font-weight: 300;
    color: var(--white);
    margin-top: 3px;
  }
  .contact-line svg { width: 11px; height: 11px; fill: var(--gold); }
</style>
</head>
<body>
  <div class="card card-front">
    <div class="front-wordmark">Gilded Vantages</div>
  </div>

  <div class="card card-back">
    <svg class="back-art" viewBox="0 0 520 297" aria-hidden="false">
      <defs>
        <linearGradient id="photoTone" x1="0" y1="0" x2="1" y2="1">
          <stop offset="0" stop-color="var(--sky)"/>
          <stop offset="0.45" stop-color="var(--foliage)"/>
          <stop offset="1" stop-color="var(--slate)"/>
        </linearGradient>
        <linearGradient id="goldSweep" x1="0" y1="0" x2="1" y2="0">
          <stop offset="0" stop-color="var(--gold)"/>
          <stop offset="1" stop-color="var(--gold-light)"/>
        </linearGradient>
      </defs>
      <path d="M195 150 C 270 215, 400 232, 520 200 L 520 214 C 400 252, 260 232, 195 150 Z" fill="url(#goldSweep)"/>
      <path d="M190 0 L 520 0 L 520 196 C 400 226, 275 205, 190 140 Z" fill="url(#photoTone)" role="img" aria-label="Photograph of a two-storey house porch fitted with dark exterior shades, pine trees and blue sky behind"/>
    </svg>
    <div class="back-wordmark">Gilded<br>Vantages</div>
    <div class="contact">
      <div class="contact-name">Daniel Forsythe</div>
      <div class="contact-role">Owner</div>
      <div class="contact-line">
        <svg viewBox="0 0 24 24"><path d="M6.6 10.8a15.1 15.1 0 0 0 6.6 6.6l2.2-2.2c.3-.3.7-.4 1-.2 1.1.4 2.3.6 3.6.6.6 0 1 .4 1 1V20c0 .6-.4 1-1 1A17 17 0 0 1 3 4c0-.6.4-1 1-1h3.5c.6 0 1 .4 1 1 0 1.3.2 2.5.6 3.6.1.3 0 .7-.2 1z"/></svg>
        <span>919-482-7034</span>
      </div>
      <div class="contact-line">
        <svg viewBox="0 0 24 24"><circle cx="12" cy="12" r="10"/></svg>
        <span>gildedvantages.com</span>
      </div>
    </div>
  </div>
</body>
</html>
```